Need design for Vinyl window signs

I need Vinyl window sign to cover my front retail pharmacy window. Not the whole window area i want there to be open areas so people can still see inside.
Attached is the pic of front door and also the logo which contains the colors we want to use. The width of the door is about 14ft wide and 7ft high and its 3 sections. The middle section the door is 36 inch.

And the vinyl graphic should include the following info:
Maplecrest Commons pharmacy
Caring for you, Caring for the community

Wellness starts here!
Locally owned independent pharmacy
No wait
Same Copay as chains
Free local delivery

We do prescriptions, private consultations, compounding, immunizations, travel health and other clinical services

We also provide free blood pressure, blood glucose and blood oxygen testing everyday.
No appointments necessary.

Write Pharmacy in different languages: Spanish, Farsi, Hebrew, Russian

Phone: 555-206-3948

Hours:
M- F 9-6
Sat and sun and major Holliday: closed

Target Market(s)

Patients: People seeking medication or health advice. Caregivers: Those caring for others who need prescriptions. Health-Conscious Individuals: People interested in preventive health measures. Chronic Condition Sufferers: Individuals managing ongoing health issues. Healthcare Professionals: Doctors and nurses who may refer patients to pharmacists.

Industry/Entity Type

Retail pharmacy

Font styles to use
Sans Serif

Colors
0054AA
0677BA
7BADD7
CADEEF
E8F1F8
00AB8E
00BBA5
67D7C9
C6EFE9
E9F9F6

Requirements
Must have
• At least 3 sections for each window left side and right side and middle area, must have Green and blue color to match my logo see attached.
Nice to have
• Like to see a pics or two of people maybe seniors and younger adults enjoying their time

```html
<!DOCTYPE html>
<html lang="en">
<head>
<meta charset="utf-8">
<title>Maplecrest Commons Pharmacy – Window Vinyl</title>
<link rel="stylesheet" href="https://fonts.googleapis.com/css2?family=Montserrat:wght@400;500;600;700;800&family=Merriweather:ital,wght@1,400&display=swap">
<style>
  :root{
    --blue-deep:#0054AA;
    --blue:#0677BA;
    --blue-light:#7BADD7;
    --blue-pale:#CADEEF;
    --green:#0DAE4B;
    --green-dark:#089440;
    --white:#FFFFFF;
    --ink:#1B1B1B;
    --stage:#EEF2F6;
  }
  *{box-sizing:border-box;margin:0;padding:0}
  html,body{width:1200px;height:960px;overflow:hidden;background:var(--stage)}
  body{font-family:"Montserrat",sans-serif;position:relative}

  .banner{position:absolute;left:40px;width:1120px;height:220px;display:flex;box-shadow:0 4px 14px rgba(0,0,0,.18)}
  .banner--top{top:238px}
  .banner--bottom{top:502px}
  .panel{position:relative;height:100%;overflow:hidden}
  .panel--wide{width:440px}
  .panel--narrow{width:240px}

  /* headline tag: white word + green word */
  .tag-title{position:absolute;display:flex;height:36px;font-size:25px;line-height:36px}
  .tag-title__light{background:var(--white);color:var(--blue);font-weight:500;padding:0 12px 0 14px}
  .tag-title__bold{background:var(--green);color:var(--white);font-weight:800;padding:0 12px}

  /* services */
  .services{background:linear-gradient(100deg,var(--blue) 0%,var(--blue-deep) 100%);color:var(--white)}
  .services .tag-title{left:28px;top:31px}
  .services__grid{position:absolute;left:27px;top:89px;display:flex;gap:22px}
  .services__col{display:flex;flex-direction:column}
  .services__col--first{gap:9px;width:126px}
  .services__col--rest{gap:9px}
  .service{display:flex;align-items:center;gap:8px;font-size:10.6px;font-weight:600;line-height:12.5px}
  .services__col--rest .service{height:28px}
  .service__icon{width:16px;height:16px;flex:none}

  /* brand */
  .brand{background:linear-gradient(135deg,#FFFFFF 0%,#EEF0F2 100%);text-align:center}
  .brand__mark{position:absolute;left:79px;top:20px;width:82px;height:82px}
  .brand__name{position:absolute;left:0;right:0;top:110px;font-size:17px;font-weight:800;color:var(--blue-deep);line-height:20px;letter-spacing:.2px}
  .brand__rule{position:absolute;left:37px;right:37px;top:161px;height:1px;background:#666}
  .brand__tagline{position:absolute;left:0;right:0;top:169px;font-family:"Merriweather",serif;font-style:italic;font-size:12px;line-height:16px;color:var(--ink)}

  /* photo areas */
  .photo{display:block}
  .photo--family{background:linear-gradient(120deg,#D9D4CD 0%,#A7A29C 40%,#C9BBA8 75%,#E5DED5 100%)}
  .photo--outdoor{background:linear-gradient(180deg,#B9C7D1 0%,#C8B38D 55%,#6E6A70 100%)}

  /* contact */
  .contact{background:var(--green);color:var(--white)}
  .phone{position:absolute;left:16px;top:52px;width:212px;height:34px;background:var(--white);border-radius:17px;display:flex;align-items:center}
  .phone__icon{width:38px;height:38px;margin-left:-2px;flex:none}
  .phone__number{font-size:22px;font-weight:800;color:var(--blue-deep);margin-left:6px;letter-spacing:-.3px}
  .hours{position:absolute;left:21px;top:116px;width:197px;height:76px;border:1.3px solid var(--white);border-radius:5px;text-align:center;font-size:10px;font-weight:500;line-height:13px}
  .hours__label{position:absolute;left:24px;top:-11px;width:149px;height:22px;background:var(--blue);border-radius:3px;font-size:13px;font-weight:800;line-height:22px}
  .hours__row{margin-top:22px}
  .hours__row + .hours__row{margin-top:5px}
  .hours strong{font-weight:700}

  /* wellness */
  .wellness{background:linear-gradient(100deg,var(--blue) 0%,var(--blue-deep) 100%);color:var(--white)}
  .wellness .tag-title{left:28px;top:25px}
  .benefit{position:absolute;font-size:13.4px;line-height:17px;font-weight:600}
  .benefit b{font-weight:800}
  .benefit--owned{left:40px;top:78px}
  .benefit--delivery{left:283px;top:78px}
  .benefit--copay{left:40px;top:129px;font-weight:700}
  .benefit--wait{left:283px;top:129px;font-weight:700}
  .divider{position:absolute;top:118px;height:1px;background:var(--white)}
  .divider--left{left:40px;width:184px}
  .divider--right{left:283px;width:119px}
  .languages{position:absolute;left:35px;top:173px;display:flex;gap:17px}
  .language{width:79px;height:25px;border-radius:13px;background:var(--green);font-size:10.5px;font-weight:700;line-height:25px;text-align:center;box-shadow:0 2px 3px rgba(0,0,0,.25)}
</style>
</head>
<body>

<section class="banner banner--top">
  <div class="panel panel--wide services">
    <h2 class="tag-title"><span class="tag-title__light">OUR</span><span class="tag-title__bold">SERVICES</span></h2>
    <div class="services__grid">
      <ul class="services__col services__col--first" style="list-style:none">
        <li class="service"><svg class="service__icon" viewBox="0 0 16 16" fill="none" stroke="#fff" stroke-width="1.2"><rect x="3" y="1.5" width="10" height="13" rx="1.5"/><path d="M5.5 5h5M5.5 8h5M5.5 11h3"/></svg>Prescriptions</li>
        <li class="service"><svg class="service__icon" viewBox="0 0 16 16" fill="none" stroke="#fff" stroke-width="1.2"><path d="M2 9a4 3 0 1 1 3 3l-2 2v-2.6"/><path d="M9 4h5v5h-2l-2 2V9H9z"/></svg>Private<br>Consultations</li>
        <li class="service"><svg class="service__icon" viewBox="0 0 16 16" fill="none" stroke="#fff" stroke-width="1.2"><circle cx="4" cy="4" r="2.3"/><circle cx="12" cy="5" r="2"/><circle cx="7" cy="12" r="2.5"/><path d="M6 5l4 0M5 6l1.5 4"/></svg>Compounding</li>
        <li class="service"><svg class="service__icon" viewBox="0 0 16 16" fill="none" stroke="#fff" stroke-width="1.2"><path d="M8 1.5l5.5 2v4c0 3.5-2.5 6-5.5 7-3-1-5.5-3.5-5.5-7v-4z"/><path d="M8 5.5v5M5.5 8h5"/></svg>Immunizations</li>
      </ul>
      <ul class="services__col services__col--rest" style="list-style:none">
        <li class="service"><svg class="service__icon" viewBox="0 0 16 16" fill="none" stroke="#fff" stroke-width="1.2"><rect x="2.5" y="4" width="9" height="10" rx="1.5"/><path d="M5 4V2h4v2M5 7v5M9 7v5"/><circle cx="12.5" cy="12" r="2.3"/></svg>Travel<br>Health Services</li>
        <li class="service"><svg class="service__icon" viewBox="0 0 16 16" fill="none" stroke="#fff" stroke-width="1.2"><rect x="2.5" y="2.5" width="10" height="12" rx="1.5"/><path d="M5.5 1.5h4v2h-4zM5 7h5M5 10h3"/><path d="M10 12l1.5 1.5L14 10"/></svg>Other<br>Clinical Services</li>
        <li class="service"><svg class="service__icon" viewBox="0 0 16 16" fill="none" stroke="#fff" stroke-width="1.2"><rect x="1.5" y="3" width="13" height="11.5" rx="1.5"/><path d="M1.5 6.5h13M5 1.5v3M11 1.5v3"/><circle cx="8" cy="10.5" r="2"/></svg>No appointments<br>necessary</li>
      </ul>
      <ul class="services__col services__col--rest" style="list-style:none">
        <li class="service"><svg class="service__icon" viewBox="0 0 16 16" fill="none" stroke="#fff" stroke-width="1.2"><circle cx="8" cy="6.5" r="5"/><path d="M8 6.5l2-2M8 11.5V15"/></svg>Free<br>Blood Pressure</li>
        <li class="service"><svg class="service__icon" viewBox="0 0 16 16" fill="none" stroke="#fff" stroke-width="1.2"><rect x="3.5" y="1.5" width="9" height="13" rx="2"/><rect x="5.5" y="4" width="5" height="4"/><circle cx="8" cy="11" r="1"/></svg>Blood<br>Glucose Testing</li>
        <li class="service"><svg class="service__icon" viewBox="0 0 16 16" fill="none" stroke="#fff" stroke-width="1.2"><rect x="3" y="1.5" width="10" height="13" rx="2"/><path d="M5 5h6M5 8h6M5 11h3"/></svg>Blood<br>Oxygen Testing</li>
      </ul>
    </div>
  </div>

  <div class="panel panel--narrow brand">
    <svg class="brand__mark" viewBox="0 0 82 82" aria-hidden="true"><circle cx="41" cy="41" r="38" fill="none" stroke="var(--blue-deep)" stroke-width="5"/></svg>
    <h1 class="brand__name">MAPLECREST COMMONS<br>PHARMACY</h1>
    <div class="brand__rule"></div>
    <p class="brand__tagline">Caring for you,<br>Caring for the community</p>
  </div>

  <div class="panel panel--wide photo photo--family" role="img" aria-label="Photo: a young mother, a boy and grandparents playing a block-stacking game on a living room rug"></div>
</section>

<section class="banner banner--bottom">
  <div class="panel panel--wide photo photo--outdoor" role="img" aria-label="Photo: seniors and a young girl and boy laughing while playing basketball outdoors"></div>

  <div class="panel panel--narrow contact">
    <div class="phone">
      <svg class="phone__icon" viewBox="0 0 38 38" aria-hidden="true"><circle cx="19" cy="19" r="19" fill="var(--blue)"/><path d="M13 11.5l3 -0.5 2 4.5-2 1.5c1 2.5 3 4.5 5.5 5.5l1.5-2 4.5 2-.5 3c-7 .5-14-6.5-14-14z" fill="none" stroke="#fff" stroke-width="1.4" stroke-linejoin="round"/></svg>
      <span class="phone__number">555-206-3948</span>
    </div>
    <div class="hours">
      <div class="hours__label">OPENING HOURS</div>
      <p class="hours__row">Monday - Friday : <strong>9:00 - 6:00</strong></p>
      <p class="hours__row">Saturday &amp; Sunday<br>and Major Holliday : <strong>Closed</strong></p>
    </div>
  </div>

  <div class="panel panel--wide wellness">
    <h2 class="tag-title"><span class="tag-title__light">WELLNESS</span><span class="tag-title__bold">STARTS HERE!</span></h2>
    <p class="benefit benefit--owned"><b>LOCALLY OWNED</b><br>Independent Pharmacy</p>
    <p class="benefit benefit--delivery"><b>FREE</b><br>Local Delivery</p>
    <div class="divider divider--left"></div>
    <div class="divider divider--right"></div>
    <p class="benefit benefit--copay">SAME COPAY as chains</p>
    <p class="benefit benefit--wait">NO Wait</p>
    <div class="languages">
      <span class="language" lang="es">farmacia</span>
      <span class="language" lang="fa" dir="rtl">داروخانه</span>
      <span class="language" lang="he" dir="rtl">בית מרקחת</span>
      <span class="language" lang="ru">Аптека</span>
    </div>
  </div>
</section>

</body>
</html>
```